Basisdesign Buch-/E-Book-Cover für Haldmoor-Krimis
Zielgruppe
Ich schreibe Krimis, Thriller, Kriminalstories, Krimiparodien.
Meine Zielgruppe sind deutschsprachige Krimi-Leser.
Aufgabenstellung
Ich benötige ein Basisdesign für Buchcover (Höhe 2.343, Breite 1.518 Pixel – Druckfalter, eBooks). Alle Bücher haben mit Crime zu tun, aber in verschiedenen Unter-Genres: Klassischer Kriminalroman, Thriller, Fantasy Thriller, Kurzgeschichten, Krimi-Parodien.
Ich benötige, quasi als Marke, dafür ein gleichbleibendes grafisches Element, z. B. einen Sockel im unteren Coverbereich, der den Autorennamen „Jonas Haldmoor“ und das jeweilige Unter-Genre enthält. Unter-Genres sind: Krimi, Thriller, Fantasy-Thriller, Kurzgeschichten und Krimi-Parodie. Das alles sollte auch noch im Format der Lesoria-Bücherlisten wie „Kunden kauften auch“ halbwegs lesbar sein.
Ein bisschen mörderisch und blutig sind alle Varianten.
Nachdem die Bandbreite vom Thriller bis zur Parodie reicht, sollte der gleichbleibende Markenbereich eine entsprechende grafische Bandbreite aufweisen, dabei aber die Grundmelodie Crime nicht aus den Augen verlieren.
Im oberen Bereich stelle ich mir Grafiken oder Hintergrundfotos vor, die für jedes Buch individuell gestaltet werden müssten, was jedoch über das Basisdesign hinausgeht. Die Wahl der Schriftart für Titel (bislang 11 – 25 Zeichen inkl. Leerzeichen) und allfällige Untertitel (im Umfang von maximal 30 Zeichen), sollte zu denen im Sockel passen.

```html
<!DOCTYPE html>
<html lang="de">
<head>
<meta charset="utf-8">
<title>Haldmoor-Krimis – Basiscover</title>
<link rel="stylesheet" href="https://fonts.googleapis.com/css2?family=Anton&family=Open+Sans:wght@700;800&family=Pathway+Gothic+One&display=swap">
<style>
  :root {
    --page: #ffffff;
    --cover-dark: #232a2d;
    --cover-mid: #3a4245;
    --sky-light: #b9b4a8;
    --sky-grey: #6f7673;
    --title-orange: #d8861f;
    --sticker-orange: #c25a14;
    --sticker-deep: #a9430e;
    --sticker-curl: #e9a53a;
    --sticker-ink: #1d1a17;
    --name-cream: #ecead6;
    --genre-red: #cc2a2c;
  }
  * { margin: 0; padding: 0; box-sizing: border-box; }
  html, body {
    width: 1200px;
    height: 848px;
    overflow: hidden;
    background: var(--page);
  }
  .cover {
    position: absolute;
    left: 354px;
    top: 44px;
    width: 492px;
    height: 760px;
    background: var(--cover-dark);
    overflow: hidden;
    box-shadow: 0 2px 6px rgba(0,0,0,0.25);
  }
  .cover-photo {
    position: absolute;
    left: 0; top: 0;
    width: 100%;
    height: 250px;
    background:
      radial-gradient(ellipse 60% 40% at 30% 55%, rgba(205,198,185,0.85), transparent 70%),
      radial-gradient(ellipse 50% 35% at 80% 60%, rgba(190,184,172,0.8), transparent 70%),
      linear-gradient(to bottom, var(--sky-grey) 0%, var(--sky-light) 55%, var(--cover-dark) 100%);
  }
  .title {
    position: absolute;
    left: 77px;
    top: 188px;
    width: 322px;
    display: flex;
    justify-content: space-between;
    font-family: "Pathway Gothic One", sans-serif;
    font-size: 164px;
    line-height: 1;
    color: var(--title-orange);
  }
  .sticker {
    position: absolute;
    left: 4px;
    top: 483px;
    width: 158px;
    height: 156px;
  }
  .sticker svg { position: absolute; inset: 0; }
  .sticker-text {
    position: absolute;
    left: 0; top: 22px;
    width: 150px;
    text-align: center;
    font-family: "Open Sans", sans-serif;
    font-weight: 700;
    color: var(--sticker-ink);
    line-height: 1.1;
  }
  .sticker-text .small { font-size: 19px; display: block; }
  .sticker-text .big { font-size: 27px; font-weight: 800; display: block; }
  .sticker-text .dots { font-size: 14px; display: block; line-height: 0.6; }
  .brand-base {
    position: absolute;
    left: 100px;
    top: 640px;
    width: 290px;
    text-align: center;
    font-family: "Anton", sans-serif;
    color: var(--name-cream);
    font-size: 72px;
    line-height: 0.78;
    letter-spacing: -1px;
    text-transform: uppercase;
  }
  .brand-base span { display: block; }
  .genre {
    position: absolute;
    left: 388px;
    top: 716px;
    font-family: "Open Sans", sans-serif;
    font-weight: 700;
    font-size: 18px;
    letter-spacing: 0.28em;
    color: var(--genre-red);
  }
</style>
</head>
<body>
  <main class="cover">
    <div class="cover-photo" role="img" aria-label="Hintergrundfoto: Eiszapfen vor wolkigem grauem Himmel, an einem hängt ein Blutstropfen"></div>

    <h1 class="title" aria-label="Titel">
      <span>T</span><span>I</span><span>T</span><span>E</span><span>L</span>
    </h1>

    <div class="sticker">
      <svg width="158" height="156" viewBox="0 0 158 156" aria-hidden="true">
        <defs>
          <radialGradient id="stickerFill" cx="45%" cy="35%" r="65%">
            <stop offset="0%" stop-color="#d06a1a"/>
            <stop offset="100%" stop-color="#a9430e"/>
          </radialGradient>
        </defs>
        <path d="M78 2 A76 76 0 1 0 82 154 L150 90 A76 76 0 0 0 78 2 Z" fill="url(#stickerFill)"/>
        <path d="M82 154 L150 90 C130 96 104 104 88 120 C84 132 82 144 82 154 Z" fill="var(--sticker-curl)"/>
      </svg>
      <p class="sticker-text">
        <span class="small">KUNDEN</span>
        <span class="big">KAUFTEN</span>
        <span class="small">AUCH</span>
        <span class="dots">....</span>
      </p>
    </div>

    <p class="brand-base"><span>Jonas</span><span>Haldmoor</span></p>
    <p class="genre">KRIMI</p>
  </main>
</body>
</html>
```